Mina Patelson

My company, velkor coaching are based in surrey uk. I am looking for a design for A5 flyer to attract coaching for children and young adults.
I want to include a an image of a mother reprimading her children - a teenager and young adult front and any releant images at back.
Also my company logo at indicated at bottom of front and back but pls do not include the word consultants - please change to coaching
FRONT:
Strapline: Do you feel you’re constantly nagging your child about their behaviour and school work? Is this affecting your relationship?
Image of mother and speech bubbles:
• How can I help my child get the results they’re capable of and make the right subject choices?
• How can I help my child think for themselves and not just follow the crowd?
• How do I get my child to achieve their best academically and socially?
• How do I help my child make the right career choice for them?
Testimonials from our client prove that Personal Development Coaching can help your child:
‘Coaching improved my self-awareness and helped me make better decisions without being influenced by my peers’.
'Mina helped me to set clear and purposeful university goals at a time that I was confused. I am now at a top university and have a clear vision of my future career path’.
‘I successfully met my yearly goals by using techniques with Velkor coaching, such as the wheel of life and vision boards’.
'Mina has given me the impetus that I was lacking to break down what I saw as unachievable academic ambition’.
'Velkor’s coaching has helped me feel motivated, energised and confident within myself'.
Book your free consultation:
e: mina@velkor-example.co.uk t: 0781 502 6634 w: www.velkor-example.co.uk (include logo)
BACK: images of children of different age groups (teenagers to young adults)
Why Velkor?
• Qualified Personal Development Coach
• Qualified teacher with 25 years experience in secondary schools and at university level
• Postgraduate qualification in teaching children with specific learning difficulties
Mina is a specialist in coaching for:
• Coping with peer and academic pressure
• Identifying strengths and building confidence
• Discovering an appropriate career path
• Feeling motivated and achieving potential
• Managing time and learning how to discipline one’s self
Updates
I would also liek to add my phot to flyer
I have extended the deadline
The flyer is a5 double sided
I will require my photo on the back - which I will upload
Logo image is provided but will designers provide other images

```html
<!DOCTYPE html>
<html lang="en">
<head>
<meta charset="utf-8">
<title>Velkor Coaching – A5 Flyer</title>
<link rel="stylesheet" href="https://fonts.googleapis.com/css2?family=Open+Sans:wght@600;700;800&family=Arimo:ital,wght@0,400;0,700;1,400&family=Tinos:wght@400&display=swap">
<style>
  :root{
    --bg:#e8e5e0;
    --paper:#ffffff;
    --blue:#3a86ec;
    --blue-text:#2f7ce0;
    --blue-deep:#1f63c4;
    --yellow:#fcd21f;
    --yellow-soft:#fde66a;
    --orange:#f07a32;
    --bubble:#5b9cf2;
    --bubble-text:#f7ec4c;
    --ink:#111111;
    --skin:#d9b59a;
    --hair:#6b4a36;
  }
  *{box-sizing:border-box;margin:0;padding:0}
  html,body{width:1200px;height:900px;overflow:hidden;background:var(--bg)}
  .canvas{position:relative;width:1200px;height:900px;overflow:hidden;background:var(--bg);font-family:"Arimo",Arial,sans-serif}
  .page{position:absolute;top:38px;width:570px;height:810px;background:var(--paper);overflow:hidden;box-shadow:0 2px 8px rgba(0,0,0,.18)}
  .page--front{left:18px}
  .page--back{left:612px;width:571px}
  .page__art{position:absolute;inset:0;width:100%;height:100%}
  .abs{position:absolute}

  /* front */
  .strapline{left:239px;top:26px;width:320px;font-family:"Open Sans",Arial,sans-serif;font-weight:600;font-size:15.5px;line-height:20px;color:var(--blue-text)}
  .strapline__question{color:var(--orange)}
  .photo{display:block}
  .bubble-text{font-family:"Tinos","Times New Roman",serif;font-size:10.5px;line-height:12px;color:var(--bubble-text);text-align:left}
  .testimonials__title{left:350px;top:212px;width:200px;font-family:"Arimo",Arial,sans-serif;font-weight:700;font-size:8.6px;line-height:10.5px;color:var(--yellow);text-transform:uppercase}
  .testimonials__box{left:348px;top:252px;width:200px;height:344px;border-left:1px solid rgba(255,255,255,.85);border-right:1px solid rgba(255,255,255,.85)}
  .testimonials__box::before,.testimonials__box::after{content:"";position:absolute;left:0;width:100%;height:10px;border-top:1px solid rgba(255,255,255,.85)}
  .testimonials__box::before{top:0}
  .testimonials__box::after{bottom:-10px}
  .testimonial-list{left:352px;top:258px;width:192px;list-style:none;color:#fff;font-style:italic;font-size:10.3px;line-height:13.4px;text-align:center}
  .testimonial-list li{margin-bottom:13px}

  .cta{font-family:"Tinos","Times New Roman",serif;font-size:23px;line-height:26px;white-space:nowrap}
  .cta--front{left:102px;top:728px;color:var(--orange)}
  .cta--back{left:104px;top:728px;color:var(--yellow)}
  .contact{display:flex;align-items:center;gap:4px;font-size:10.6px;white-space:nowrap}
  .contact svg{width:10px;height:10px;flex:none}
  .contact--front{left:70px;top:753px;color:var(--blue-text)}
  .contact--back{left:72px;top:753px;color:#fff}
  .brand{display:flex;flex-direction:column;align-items:center;font-family:"Tinos","Times New Roman",serif;font-size:15px;line-height:17px;letter-spacing:.5px;color:var(--blue-deep)}
  .brand__dot{width:16px;height:16px;border-radius:50%;background:var(--blue-deep);margin-bottom:6px}
  .brand--front{left:420px;top:690px}
  .brand--back{left:420px;top:690px;color:#fff}
  .brand--back .brand__dot{background:#fff}

  /* back */
  .why-title{left:61px;top:52px;font-family:"Open Sans",Arial,sans-serif;font-weight:800;font-size:37px;letter-spacing:1px;color:var(--blue-text)}
  .credential{left:0;width:389px;height:54px;background:var(--yellow);border-radius:0 27px 27px 0;display:flex;align-items:center;padding-left:62px;font-weight:700;font-size:13.3px;line-height:17px;color:var(--ink)}
  .specialist-title{left:54px;top:420px;font-family:"Open Sans",Arial,sans-serif;font-weight:700;font-size:18.5px;color:var(--blue-text)}
  .specialisms{left:222px;top:462px;width:308px;list-style:none}
  .specialisms li{position:relative;padding-left:30px;font-weight:700;font-size:11.2px;line-height:14px;color:var(--ink);min-height:28px}
  .specialisms svg{position:absolute;left:0;top:-2px;width:17px;height:17px}
</style>
</head>
<body>
<main class="canvas">

  <!-- FRONT -->
  <section class="page page--front" aria-label="Flyer front">
    <svg class="page__art" viewBox="0 0 570 810" preserveAspectRatio="none" aria-hidden="true">
      <defs>
        <clipPath id="front-blue-area">
          <path d="M0,200 C140,222 360,190 570,138 L570,612 C400,618 200,640 0,676 Z"/>
        </clipPath>
        <linearGradient id="front-face-tone" x1="0" x2="1" y1="0" y2="0">
          <stop offset="0" stop-color="#c9a58c"/>
          <stop offset="0.45" stop-color="#e6cdb9"/>
          <stop offset="0.8" stop-color="#eef2fb"/>
          <stop offset="1" stop-color="#3a86ec"/>
        </linearGradient>
        <linearGradient id="front-hair-tone" x1="0" x2="0" y1="0" y2="1">
          <stop offset="0" stop-color="#e6cdb9" stop-opacity="0"/>
          <stop offset="1" stop-color="#7a5840"/>
        </linearGradient>
      </defs>
      <path d="M0,112 C150,160 360,150 570,112 L570,150 C380,196 150,226 0,200 Z" fill="var(--yellow)"/>
      <path d="M0,200 C140,222 360,190 570,138" fill="none" stroke="var(--orange)" stroke-width="2"/>
      <rect x="0" y="130" width="570" height="560" fill="var(--blue)" clip-path="url(#front-blue-area)"/>
      <g clip-path="url(#front-blue-area)">
        <rect x="0" y="130" width="345" height="560" fill="url(#front-face-tone)"/>
        <rect x="0" y="430" width="300" height="260" fill="url(#front-hair-tone)"/>
      </g>
      <path d="M0,676 C200,640 400,618 570,612 L570,664 C390,672 190,700 0,728 Z" fill="var(--yellow)"/>
      <path d="M0,676 C200,640 400,618 570,612" fill="none" stroke="var(--orange)" stroke-width="2"/>
      <!-- speech bubbles -->
      <g fill="var(--bubble)">
        <ellipse cx="274" cy="253" rx="78" ry="37"/>
        <ellipse cx="276" cy="355" rx="72" ry="33"/>
        <ellipse cx="272" cy="440" rx="62" ry="36"/>
        <ellipse cx="222" cy="518" rx="62" ry="32"/>
        <circle cx="199" cy="298" r="6"/><circle cx="187" cy="310" r="4.5"/><circle cx="178" cy="320" r="3"/>
        <circle cx="203" cy="376" r="5"/><circle cx="192" cy="384" r="4"/><circle cx="182" cy="390" r="3"/>
        <circle cx="205" cy="425" r="5"/><circle cx="192" cy="414" r="4"/><circle cx="181" cy="405" r="3"/>
        <circle cx="170" cy="487" r="5"/><circle cx="161" cy="475" r="4"/><circle cx="154" cy="465" r="3"/>
      </g>
    </svg>

    <div class="abs photo" role="img" aria-label="Photo of a mother reprimanding her teenage daughter" style="left:38px;top:12px;width:200px;height:140px;background:linear-gradient(90deg,#e9c4a4 0%,#f3d9a0 35%,#5aa9d6 60%,#6a4a38 100%);border-radius:4px"></div>
    <div class="abs" role="img" aria-label="Close-up photo of a mother holding her child, looking thoughtful" style="left:0;top:200px;width:1px;height:1px"></div>

    <p class="abs strapline">Do you feel you’re constantly nagging your child about their behaviour and school work?<br><span class="strapline__question">Is this affecting your relationship?</span></p>

    <p class="abs bubble-text" style="left:212px;top:229px;width:128px;text-align:center">How can I help my child get the results they’re capable of and make the right subject choices?</p>
    <p class="abs bubble-text" style="left:213px;top:335px;width:124px">How can I help my child think for themselves and not just follow the crowd?</p>
    <p class="abs bubble-text" style="left:219px;top:414px;width:108px">How do I get my child to achieve their best academically and socially?</p>
    <p class="abs bubble-text" style="left:172px;top:500px;width:104px">How do I help my child make the right career choice for them?</p>

    <p class="abs testimonials__title">Testimonials from our client prove that personal development coaching can help your child:</p>
    <div class="abs testimonials__box" aria-hidden="true"></div>
    <ul class="abs testimonial-list">
      <li>‘Coaching improved my self-awareness and helped me make better decisions without being influenced by my peers’.</li>
      <li>'Mina helped me to set clear and purposeful university goals at a time that I was confused. I am now at a top university and have a clear vision of my future career path’.</li>
      <li>‘I successfully met my yearly goals by using techniques with Velkor coaching, such as the wheel of life and vision boards’.</li>
      <li>'Mina has given me the impetus that I was lacking to break down what I saw as unachievable academic ambition’.</li>
      <li>'Velkor’s coaching has helped me feel motivated, energised and confident within myself'.</li>
    </ul>

    <p class="abs cta cta--front">Book your free consultation</p>
    <p class="abs contact contact--front">
      <svg viewBox="0 0 10 10"><rect x="0.5" y="1.5" width="9" height="7" fill="none" stroke="var(--orange)"/><path d="M0.5,1.5 L5,5.5 L9.5,1.5" fill="none" stroke="var(--orange)"/></svg>
      <span>mina@velkor-example.co.uk</span>
      <svg viewBox="0 0 10 10"><rect x="3" y="0.5" width="4" height="9" rx="1" fill="var(--orange)"/></svg>
      <span>0781 502 6634</span>
      <svg viewBox="0 0 10 10"><circle cx="5" cy="5" r="4.5" fill="var(--orange)"/><path d="M0.5,5 H9.5 M5,0.5 V9.5" stroke="#fff" stroke-width=".8"/></svg>
      <span>www.velkor-example.co.uk</span>
    </p>
    <div class="abs brand brand--front"><span class="brand__dot"></span><span>VELKOR</span><span>COACHING</span></div>
  </section>

  <!-- BACK -->
  <section class="page page--back" aria-label="Flyer back">
    <svg class="page__art" viewBox="0 0 571 810" preserveAspectRatio="none" aria-hidden="true">
      <path d="M0,676 C180,650 380,622 571,612 L571,666 C390,672 190,700 0,732 Z" fill="var(--yellow)"/>
      <path d="M0,678 C180,652 380,624 571,614" fill="none" stroke="#fff" stroke-width="2"/>
      <path d="M0,732 C190,700 390,672 571,666 L571,810 L0,810 Z" fill="var(--blue)"/>
      <path d="M0,732 C190,700 390,672 571,666" fill="none" stroke="#fff" stroke-width="2"/>
    </svg>

    <div class="abs photo" role="img" aria-label="Photo of a group of teenagers and young adults" style="left:323px;top:26px;width:248px;height:188px;background:linear-gradient(180deg,#ffffff 0%,#d9c6b4 25%,#c9a070 45%,#7fa6c9 70%,#ffffff 100%);border-radius:6px"></div>

    <h1 class="abs why-title">WHY VELKOR?</h1>
    <p class="abs credential" style="top:120px">Qualified Personal Development Coach</p>
    <p class="abs credential" style="top:207px">Qualified teacher with 25 years experience<br>in secondary schools and at university level</p>
    <p class="abs credential" style="top:295px">Postgraduate qualification in teaching<br>children with specific learning difficulties</p>

    <h2 class="abs specialist-title">Mina is a specialist in coaching for:</h2>
    <div class="abs photo" role="img" aria-label="Portrait photo of coach Mina Patelson" style="left:54px;top:462px;width:140px;height:212px;background:linear-gradient(180deg,#f1ece8 0%,#b5673f 30%,#d9b59a 45%,#2a2a2a 80%,#efebe7 100%)"></div>
    <ul class="abs specialisms">
      <li><svg viewBox="0 0 17 17"><circle cx="8.5" cy="9" r="7" fill="var(--yellow)"/><path d="M4.5,8.5 L8,12 L15,3" fill="none" stroke="var(--blue-deep)" stroke-width="2.2"/></svg>Coping with peer and academic pressure</li>
      <li><svg viewBox="0 0 17 17"><circle cx="8.5" cy="9" r="7" fill="var(--yellow)"/><path d="M4.5,8.5 L8,12 L15,3" fill="none" stroke="var(--blue-deep)" stroke-width="2.2"/></svg>Identifying strengths and building confidence</li>
      <li><svg viewBox="0 0 17 17"><circle cx="8.5" cy="9" r="7" fill="var(--yellow)"/><path d="M4.5,8.5 L8,12 L15,3" fill="none" stroke="var(--blue-deep)" stroke-width="2.2"/></svg>Discovering an appropriate career path</li>
      <li><svg viewBox="0 0 17 17"><circle cx="8.5" cy="9" r="7" fill="var(--yellow)"/><path d="M4.5,8.5 L8,12 L15,3" fill="none" stroke="var(--blue-deep)" stroke-width="2.2"/></svg>Feeling motivated and achieving potential</li>
      <li><svg viewBox="0 0 17 17"><circle cx="8.5" cy="9" r="7" fill="var(--yellow)"/><path d="M4.5,8.5 L8,12 L15,3" fill="none" stroke="var(--blue-deep)" stroke-width="2.2"/></svg>Managing time and learning how to discipline one’s self</li>
    </ul>

    <p class="abs cta cta--back">Book your free consultation</p>
    <p class="abs contact contact--back">
      <svg viewBox="0 0 10 10"><rect x="0.5" y="1.5" width="9" height="7" fill="none" stroke="var(--orange)"/><path d="M0.5,1.5 L5,5.5 L9.5,1.5" fill="none" stroke="var(--orange)"/></svg>
      <span>mina@velkor-example.co.uk</span>
      <svg viewBox="0 0 10 10"><rect x="3" y="0.5" width="4" height="9" rx="1" fill="var(--orange)"/></svg>
      <span>0781 502 6634</span>
      <svg viewBox="0 0 10 10"><circle cx="5" cy="5" r="4.5" fill="var(--orange)"/><path d="M0.5,5 H9.5 M5,0.5 V9.5" stroke="#fff" stroke-width=".8"/></svg>
      <span>www.velkor-example.co.uk</span>
    </p>
    <div class="abs brand brand--back"><span class="brand__dot"></span><span>VELKOR</span><span>COACHING</span></div>
  </section>

</main>
</body>
</html>
```